Business Cards for IT Consulting Company (Managed Service Provider)

I am looking to have some business cards printed and would like some designs. We are an IT Consulting company based in Vancouver BC. I would like a nice clean and modern look to the cards. I have uploaded all the versions of my logo so parts can be used as needed. Here is a snippit from our website homepage:

Kelbrook Systems Ltd. is an IT Solutions Partner located in Vancouver BC, Canada. We offer IT solutions and support to customers in the greater Vancouver Area. With expertise in Microsoft platforms, as well as Linux and Mac OSX and over 12 years experience in the IT industry, Kelbrook Systems is dedicated to offering our clients top quality service and products. We take pride in the solutions we offer our customers. The greatest compliment a client can give us is to recommend our services.

Kelbrook Systems Ltd. offers a wide range of IT services from onsite service to remote support and managed service solutions. This allows clients to choose the support path that best suits their company’s needs. Supporting many different sized companies from small to enterprise level over the past 12 years Kelbrook Systems has the experience and expertise needed to ensure things run smoothly. Allowing our clients to focus on doing business.

Rethinking the way IT support reaches your team.

Kelbrook Systems is dedicated to providing our clients with IT solutions that work and grow with them for years to come. This philosophy helps save money in the long run instead of replacing equipment constantly. Far too often IT solutions are not well thought out and while possibly solving the problem at hand, require replacement due to growth or quality within a very short time frame. Kelbrook Systems takes pride in providing solutions that will last and be able to accommodate growth without the need for replacement.

Industry/Entity Type

Information Technology

Contact Information for Business Card

Kelbrook Systems Ltd.
(Employee Name)
Eml: (Employees Email Address)
Web: kelbrook.me
Ph: 604-555-0142

Font styles to use
Serif
Sans Serif

Requirements
Must have
• The Company logo and company colors.
Nice to have
• - Our tag line: "Revolutionizing IT Services" or "Rethinking the way IT support reaches your team."
• - Also I really like the idea of nature and technology together blending which is sort of where my logo came from so integrating that somehow onto the business cards would be great.

```html
<!DOCTYPE html>
<html lang="en">
<head>
<meta charset="UTF-8">
<title>Kelbrook Systems Ltd. – Business Cards</title>
<link href="https://fonts.googleapis.com/css2?family=Titillium+Web:wght@300;400;600;700&display=swap" rel="stylesheet">
<style>
  :root {
    --canvas: #ecebe8;
    --card-white: #ffffff;
    --brand-blue: #23a8e0;
    --brand-blue-deep: #1a8cc0;
    --brand-green: #8dc63f;
    --band-grey: #6d6e70;
    --text-light: #ffffff;
    --shadow: rgba(0, 0, 0, 0.18);
  }
  * { box-sizing: border-box; margin: 0; padding: 0; }
  html, body {
    width: 1200px;
    height: 1200px;
    overflow: hidden;
    background: var(--canvas);
    font-family: "Titillium Web", sans-serif;
  }
  .sheet {
    position: relative;
    width: 1200px;
    height: 1200px;
  }
  .card {
    position: absolute;
    left: 290px;
    width: 620px;
    height: 352px;
    box-shadow: 0 6px 18px var(--shadow);
    overflow: hidden;
  }

  /* Front */
  .card-front {
    top: 190px;
    background: var(--card-white);
  }
  .brand-lockup {
    position: absolute;
    top: 0;
    left: 0;
    right: 0;
    bottom: 44px;
    display: flex;
    align-items: center;
    justify-content: center;
    gap: 16px;
  }
  .brand-mark {
    width: 34px;
    height: 34px;
    background: var(--brand-blue);
  }
  .brand-name {
    font-weight: 600;
    font-size: 44px;
    color: var(--brand-blue);
    letter-spacing: 0.5px;
  }
  .tagline-band {
    position: absolute;
    left: 0;
    right: 0;
    bottom: 0;
    height: 44px;
    background: var(--band-grey);
    display: flex;
    align-items: center;
    justify-content: center;
    color: var(--text-light);
    font-size: 15px;
    font-weight: 400;
    letter-spacing: 2.4px;
    white-space: nowrap;
  }

  /* Back */
  .card-back {
    top: 640px;
    background: var(--brand-blue);
    color: var(--text-light);
  }
  .contact {
    position: absolute;
    left: 54px;
    top: 64px;
  }
  .employee-name {
    font-weight: 700;
    font-size: 22px;
    letter-spacing: 0.5px;
    margin-bottom: 30px;
  }
  .contact-line {
    font-weight: 300;
    font-size: 19px;
    line-height: 1.3;
  }
  .corner-pattern {
    position: absolute;
    right: 0;
    bottom: 0;
    width: 240px;
    height: 260px;
    background: radial-gradient(circle at 100% 100%,
      rgba(141, 198, 63, 0.45) 0%,
      rgba(26, 140, 192, 0.6) 40%,
      rgba(35, 168, 224, 0) 70%);
  }
</style>
</head>
<body>
  <main class="sheet">
    <section class="card card-front">
      <div class="brand-lockup">
        <span class="brand-mark"></span>
        <span class="brand-name">Kelbrook Systems</span>
      </div>
      <div class="tagline-band">Rethinking the way IT support reaches your team.</div>
    </section>

    <section class="card card-back">
      <div class="contact">
        <p class="employee-name">ABC XYZ</p>
        <p class="contact-line">Eml: (Employees Email Address)</p>
        <p class="contact-line">Web: kelbrook.me</p>
        <p class="contact-line">Ph: 604-555-0142</p>
      </div>
      <div class="corner-pattern" role="img" aria-label="Decorative cluster of outlined hexagonal cubes with green accents"></div>
    </section>
  </main>
</body>
</html>
```